GLIMMERCUP SHAVED ICE FOOD TRUCK WEBSITE

SHAVED ICE MOBILE FOOD TRUCK WEBSITE WITH CONTENT AND MENU... SOCIALS ECT, WE ARE A MOBILE SHAVED ICE TRAILER THAT WILL BE WORKING PRIVATE EVENT'S, LOCAL EVENTS, SPORTING EVENTS AND CAN BE BOOKED OUT FOR PRIVATE PARTIES AND CORPERATE EVENTS

Target Market(s)

BIRTHDAYS, EVENTS,

Industry/Entity Type

SHAVED ICE FOOD TRUCK

Coding

Coded - Design and coding required

Number of Pages Required

4 page

Font styles to use
Serif

Colors
0054AA
0677BA
7BADD7
CADEEF
E8F1F8
0094D4
00A9DD
6FCCEA
C7EBF8
E9F6FB
EE7325
F08F49
F5BC92
FAE3D3
FDF4ED
EB3D1F
EC4F4E
F09395
F8D3D4
FCEDEE
E54698
E96AAD
F1A4CE
F9D9EA
FCEFF6

Requirements
Must have
• MY BRANDING THOUGH OUT THE WEBSITE AND FUN COOL THEME, NEED TO BE ABLE TO BOOK AN EVENT OR PARTY ONLINE AND LET PPL KNOW WHERE WE ARE AS WE ARE A MOBLIE UUNIT, NEEDS MENU
Nice to have
• A COOL FUN LOOK USING MY BRANDING AND LOGO WITH OUR CHARACTERS

```html
<!DOCTYPE html>
<html lang="en">
<head>
<meta charset="utf-8">
<title>Glimmercup Shaved Ice</title>
<link href="https://fonts.googleapis.com/css2?family=Bebas+Neue&family=Dancing+Script:wght@700&family=Poppins:wght@400;500;600&display=swap" rel="stylesheet">
<style>
:root{
  --cyan:#1cc6d3;
  --hot-red:#f5054f;
  --yellow:#ffe419;
  --navy:#0054aa;
  --blue:#0677ba;
  --sky:#0094d4;
  --ice:#e9f6fb;
  --pale-ice:#c7ebf8;
  --orange:#ee7325;
  --red:#eb3d1f;
  --pink:#e54698;
  --pink-soft:#f9d9ea;
  --cream:#fdf4ed;
  --ink:#1c1c1c;
  --grey:#6b6b6b;
  --white:#ffffff;
}
*{box-sizing:border-box;margin:0;padding:0}
html,body{width:1200px;height:3914px;overflow:hidden}
body{position:relative;font-family:"Poppins",sans-serif;color:var(--ink);background:var(--white)}
.abs{position:absolute}
.script{font-family:"Dancing Script",cursive;font-weight:700}
.btn{position:absolute;display:flex;align-items:center;justify-content:center;border-radius:30px;font-size:14px;font-weight:500;color:var(--white)}
.ph{position:absolute;border-radius:14px}

/* hero */
.hero{position:absolute;left:0;top:0;width:1200px;height:665px;background:var(--cyan);overflow:hidden}
.nav-link{position:absolute;top:24px;font-family:"Bebas Neue",sans-serif;font-size:20px;color:var(--white);letter-spacing:.5px}
.nav-book{position:absolute;left:904px;top:17px;width:108px;height:40px;border-radius:20px;background:var(--yellow);font-family:"Bebas Neue",sans-serif;font-size:19px;color:var(--ink);display:flex;align-items:center;justify-content:center}
.brand-mark{position:absolute;left:497px;top:110px;width:200px;text-align:center;color:var(--white)}
.brand-mark .name{font-weight:600;font-size:26px;letter-spacing:1px;line-height:1.2}
.brand-mark .tag{font-family:"Dancing Script",cursive;font-size:18px}
.hero-title{position:absolute;left:300px;width:600px;text-align:center;color:var(--white);font-family:"Bebas Neue",sans-serif}
.hero-title.big{top:232px;font-size:88px;line-height:1}
.hero-title.line{font-size:56px;line-height:1}
.hero-title .hl{color:var(--yellow)}
.hero-book{position:absolute;left:526px;top:452px;width:122px;height:44px;border-radius:22px;background:var(--yellow);font-family:"Bebas Neue",sans-serif;font-size:21px;color:var(--ink);display:flex;align-items:center;justify-content:center}

/* about */
.about-visual{position:absolute;left:112px;top:759px;width:456px;height:456px;border-radius:50%;background:var(--ice);display:flex;flex-direction:column;align-items:center;justify-content:center;color:var(--navy)}
.about-visual .name{font-weight:600;font-size:44px;letter-spacing:2px}
.about-visual .tag{font-family:"Dancing Script",cursive;font-size:24px;color:var(--sky)}
.about-title{position:absolute;left:664px;top:778px;font-size:48px;color:var(--red)}
.about-copy{position:absolute;left:664px;top:856px;width:440px;font-size:12.5px;line-height:25px;color:#555}
.about-copy p+p{margin-top:17px}

/* menu */
.menu-title{position:absolute;left:0;width:1200px;top:1390px;text-align:center;font-size:48px;color:var(--pink)}
.menu-card{position:absolute;top:1489px;width:226px;height:254px;border-radius:10px;background:var(--white)}
.menu-card .shot{position:absolute;left:50px;top:30px;width:126px;height:195px;border-radius:14px}
.menu-label{position:absolute;top:1766px;font-size:12px;color:var(--grey);white-space:nowrap}
.menu-name{position:absolute;top:1788px;font-size:17px;font-weight:600;color:var(--ink);white-space:nowrap}
.arrow-btn{position:absolute;top:1592px;width:48px;height:48px;border-radius:50%;display:flex;align-items:center;justify-content:center}

/* events */
.events-title{position:absolute;left:0;width:1200px;top:2130px;text-align:center;font-size:48px;color:var(--white)}
.event-card{position:absolute;width:473px;height:208px;background:var(--white);border-radius:6px}
.event-card .icon{position:absolute;left:22px;top:22px;width:70px;height:70px;border-radius:50%;background:var(--pink-soft)}
.event-card h3{position:absolute;left:110px;top:42px;font-size:20px;font-weight:600}
.event-card p{position:absolute;left:22px;top:116px;width:420px;font-size:12.5px;line-height:25px;color:#555}

/* reviews */
.reviews-title{position:absolute;left:0;width:1200px;top:2938px;text-align:center;font-size:48px;color:var(--navy)}
.review{position:absolute;top:3041px;width:310px;height:240px;background:var(--white);border-radius:6px;box-shadow:0 4px 18px rgba(0,0,0,.08)}
.review .avatar{position:absolute;left:22px;top:22px;width:56px;height:56px;border-radius:50%;background:#b98c6c}
.review .who{position:absolute;left:94px;top:30px;font-size:14px;font-weight:600}
.review .date{position:absolute;left:94px;top:54px;font-size:11px;color:var(--grey)}
.review .badge{position:absolute;right:22px;top:36px;width:24px;height:24px;border-radius:50%;background:#e4e4e4}
.review .stars{position:absolute;left:22px;top:100px;color:var(--orange);font-size:17px;letter-spacing:3px}
.review p{position:absolute;left:22px;top:130px;width:264px;font-size:12.5px;line-height:23px;color:#555}
.dot{position:absolute;top:3326px;width:8px;height:8px;border-radius:50%;background:#c9c9c9}

/* footer */
.footer-brand{position:absolute;left:108px;top:3620px;width:196px;text-align:center;color:var(--white)}
.footer-brand .name{font-weight:600;font-size:28px;letter-spacing:1px}
.footer-brand .tag{font-family:"Dancing Script",cursive;font-size:20px}
.footer-rule{position:absolute;top:3540px;width:1px;height:230px;background:rgba(255,255,255,.35)}
.footer-head{position:absolute;top:3590px;font-size:17px;font-weight:600;color:var(--ink)}
.footer-link{position:absolute;font-size:12.5px;color:var(--ink)}
.footer-icon{position:absolute;width:32px;height:32px;border-radius:50%;background:var(--white);display:flex;align-items:center;justify-content:center}
.copyright{position:absolute;left:0;width:1200px;top:3858px;text-align:center;font-size:13px;color:var(--ink)}
</style>
</head>
<body>

<header class="hero">
  <svg class="abs" style="left:0;top:0" width="1200" height="665" viewBox="0 0 1200 665">
    <polygon points="91,0 1109,0 600,638" fill="var(--hot-red)"/>
    <line x1="0" y1="380" x2="110" y2="290" stroke="var(--yellow)" stroke-width="4"/>
    <line x1="870" y1="205" x2="1065" y2="0" stroke="var(--yellow)" stroke-width="4"/>
    <line x1="320" y1="665" x2="380" y2="610" stroke="var(--yellow)" stroke-width="4"/>
  </svg>
  <div class="ph" role="img" aria-label="Candy decoration" style="left:120px;top:62px;width:115px;height:115px;background:#4b54e6"></div>
  <div class="ph" role="img" aria-label="Candy decoration" style="left:330px;top:535px;width:120px;height:110px;background:#f5a030"></div>
  <div class="ph" role="img" aria-label="Gummy candy decoration" style="left:782px;top:440px;width:88px;height:110px;background:#e5203a"></div>
  <div class="ph" role="img" aria-label="Surfing character mascot" style="left:0;top:185px;width:130px;height:150px;background:linear-gradient(135deg,#f6a3c6,#3aa3d6)"></div>
  <div class="ph" role="img" aria-label="Character mascots with surfboard" style="left:1050px;top:30px;width:150px;height:175px;background:linear-gradient(135deg,#f7b1cf,#f07a35)"></div>
  <div class="ph" role="img" aria-label="Cookies and cream shaved ice cup" style="left:96px;top:258px;width:200px;height:365px;background:linear-gradient(#d8c8a8,#1665b8)"></div>
  <div class="ph" role="img" aria-label="Red and blue shaved ice cup" style="left:972px;top:296px;width:198px;height:327px;background:linear-gradient(#e83a34,#1665b8)"></div>

  <nav>
    <span class="nav-link" style="left:264px">Home</span>
    <span class="nav-link" style="left:335px">About Us</span>
    <span class="nav-link" style="left:433px">Menu</span>
    <span class="nav-link" style="left:709px">Events</span>
    <span class="nav-link" style="left:793px">Contact Us</span>
    <span class="nav-book">Book Now</span>
  </nav>
  <div class="brand-mark"><div class="name">GLIMMERCUP</div><div class="tag">The Coolest Treats</div></div>

  <h1 class="hero-title big">GLIMMERCUP</h1>
  <div class="hero-title line" style="top:326px">Ice Creams Created</div>
  <div class="hero-title line" style="top:380px">With <span class="hl">Love Fun!</span></div>
  <div class="hero-book">Book Now</div>
</header>

<section class="about">
  <div class="about-visual" role="img" aria-label="Glimmercup brand badge"><div class="name">GLIMMERCUP</div><div class="tag">Shaved Ice</div></div>
  <h2 class="about-title script">About Glimmercup</h2>
  <div class="about-copy">
    <p>We are a mobile shaved ice truck, serving up refreshing treats at events, parties, and celebrations of all kinds. Our trailer travels to local events, private parties, and corporate gatherings, bringing the fun to you. With easy online booking, we make it simple to add a cool, delicious twist to your next event. Wherever you are, we'll bring the icy goodness straight to your door!</p>
    <p>We are a mobile shaved ice truck, offering refreshing treats for events, parties, and corporate gatherings. With easy online booking, we bring the fun and flavor directly to your next celebration!</p>
  </div>
  <div class="btn" style="left:664px;top:1144px;width:150px;height:44px;background:var(--red);box-shadow:0 4px 10px rgba(235,61,31,.3)">Learn More</div>
</section>

<section class="menu">
  <svg class="abs" style="left:0;top:1290px" width="1200" height="800" viewBox="0 0 1200 800">
    <path d="M0,135 C250,30 700,-20 1200,85 L1200,700 L0,700 Z" fill="var(--cream)"/>
    <path d="M0,135 C250,30 700,-20 1200,85 L1200,98 C700,-5 250,45 0,155 Z" fill="var(--sky)"/>
  </svg>
  <h2 class="menu-title script">Refreshing Shaved Ice Menu</h2>

  <div class="menu-card" style="left:-15px"><div class="shot" role="img" aria-label="Banana shaved ice cup" style="background:linear-gradient(#e8ddc4,#3c96d6)"></div></div>
  <div class="menu-card" style="left:240px"><div class="shot" role="img" aria-label="Blue raspberry shaved ice cup" style="background:linear-gradient(#1a6fd0,#3c96d6)"></div></div>
  <div class="menu-card" style="left:494px"><div class="shot" role="img" aria-label="Rootbeer float shaved ice cup" style="background:linear-gradient(#e53a33,#3c96d6)"></div></div>
  <div class="menu-card" style="left:747px"><div class="shot" role="img" aria-label="Layered blue and pink shaved ice cup" style="background:linear-gradient(#7aa6e8,#3c96d6)"></div></div>
  <div class="menu-card" style="left:1003px"><div class="shot" role="img" aria-label="Orange slushie cup" style="background:linear-gradient(#f29a4e,#3c96d6)"></div></div>

  <div class="arrow-btn" style="left:42px;background:var(--white);box-shadow:0 2px 8px rgba(0,0,0,.15)"><svg width="20" height="14" viewBox="0 0 20 14"><path d="M19 7H2M7 1L1 7l6 6" fill="none" stroke="#1c1c1c" stroke-width="2"/></svg></div>
  <div class="arrow-btn" style="left:1110px;background:var(--ink)"><svg width="20" height="14" viewBox="0 0 20 14"><path d="M1 7h17M13 1l6 6-6 6" fill="none" stroke="#fff" stroke-width="2"/></svg></div>

  <span class="menu-label" style="left:-15px;width:120px;overflow:hidden;direction:rtl;text-align:left">Shaved Ice Flavour</span>
  <span class="menu-name" style="left:0">anana</span>
  <span class="menu-label" style="left:240px">Shaved Ice Flavour</span>
  <span class="menu-name" style="left:240px">Blue Raspberry</span>
  <span class="menu-label" style="left:494px">Glimmercup Favorites Shaved Ice</span>
  <span class="menu-name" style="left:494px">Rootbeer Float</span>
  <span class="menu-label" style="left:747px">Glimmercup Favorites Shaved Ice</span>
  <span class="menu-name" style="left:747px">The Tidewave</span>
  <span class="menu-label" style="left:1003px;color:#9a9a9a">Glimmercup Slushies</span>
  <span class="menu-name" style="left:1003px;color:#6b6b6b">Polar Swirl</span>

  <div class="btn" style="left:512px;top:1870px;width:176px;height:42px;background:var(--pink);box-shadow:0 4px 10px rgba(229,70,152,.3)">View Full Menu</div>
</section>

<section class="events">
  <svg class="abs" style="left:0;top:1990px" width="1200" height="930" viewBox="0 0 1200 930">
    <path d="M0,20 C300,110 700,130 1200,20 L1200,850 C900,830 600,790 300,830 C150,850 60,880 0,905 Z" fill="var(--pink)"/>
    <path d="M0,20 C300,110 700,130 1200,20 L1200,42 C700,150 300,132 0,40 Z" fill="var(--navy)"/>
    <g fill="#fff" opacity=".7">
      <circle cx="40" cy="180" r="3"/><circle cx="210" cy="300" r="2.5"/><circle cx="1130" cy="230" r="3"/><circle cx="1170" cy="520" r="3"/>
      <circle cx="20" cy="620" r="3"/><circle cx="1100" cy="720" r="3"/><circle cx="80" cy="760" r="3"/><circle cx="960" cy="110" r="2.5"/>
      <circle cx="600" cy="160" r="2"/><circle cx="320" cy="110" r="2.5"/>
    </g>
  </svg>
  <div class="ph" role="img" aria-label="Group of shaved ice character mascots" style="left:10px;top:1845px;width:260px;height:185px;background:linear-gradient(135deg,#f08fb8,#2c8fd6)"></div>
  <div class="ph" role="img" aria-label="Character mascot with surfboard" style="left:975px;top:1885px;width:175px;height:160px;background:linear-gradient(135deg,#f4a7c9,#0094d4)"></div>

  <h2 class="events-title script">Book Us for Your Next Event!</h2>

  <article class="event-card" style="left:112px;top:2233px"><span class="icon"></span><h3>Private Events</h3><p>Book us for your next private party! We'll bring our mobile shaved ice truck to your event, adding a cool, refreshing treat to your special celebration.</p></article>
  <article class="event-card" style="left:614px;top:2233px"><span class="icon" style="background:var(--cream)"></span><h3>Local Events</h3><p>Catch us at local events! We're a regular at community gatherings, festivals, and fairs, serving up delicious shaved ice to keep everyone cool and happy.</p></article>
  <article class="event-card" style="left:112px;top:2470px"><span class="icon" style="background:#fcedee"></span><h3>Sporting Events</h3><p>Beat the heat at sporting events with our shaved ice! From kids' games to big tournaments, we provide refreshing treats to fuel the fun and excitement.</p></article>
  <article class="event-card" style="left:614px;top:2470px"><span class="icon" style="background:var(--pink-soft)"></span><h3>Corporate Events</h3><p>Make your corporate event memorable with our shaved ice truck. Ideal for company picnics, team-building, and celebrations, we bring fun and flavor to your workplace!</p></article>

  <div class="btn" style="left:392px;top:2735px;width:185px;height:44px;background:var(--navy)">Book Your Event</div>
  <div class="btn" style="left:614px;top:2735px;width:194px;height:44px;background:var(--white);color:var(--navy)">Explore All Events</div>
</section>

<section class="reviews">
  <h2 class="reviews-title script">Our Customers About Us</h2>
  <article class="review" style="left:112px"><span class="avatar"></span><span class="who">Seabreeze Jo</span><span class="date">2/12/2024</span><span class="badge"></span><span class="stars">★★★★★</span><p>Amazing experience! The shaved ice was a huge hit at our corporate event, and the team made everything so easy. Highly recommend!</p></article>
  <article class="review" style="left:445px"><span class="avatar" style="background:#5a3b2a"></span><span class="who">Tariq Omondi</span><span class="date">2/12/2024</span><span class="badge"></span><span class="stars">★★★★★</span><p>Amazing experience! The shaved ice was a huge hit at our corporate event, and the team made everything so easy. Highly recommend!</p></article>
  <article class="review" style="left:776px"><span class="avatar" style="background:#3a2a22"></span><span class="who">Dellan Marrow</span><span class="date">2/12/2024</span><span class="badge"></span><span class="stars">★★★★★</span><p>They were a big hit at our local fair! Super friendly and the shaved ice was the perfect treat for a hot day!"</p></article>
  <span class="dot" style="left:550px"></span>
  <span class="dot" style="left:572px"></span>
  <span class="abs" style="left:592px;top:3322px;width:16px;height:16px;border-radius:50%;border:2px solid var(--navy)"></span>
  <span class="abs" style="left:597px;top:3327px;width:6px;height:6px;border-radius:50%;background:var(--navy)"></span>
  <span class="dot" style="left:620px"></span>
  <span class="dot" style="left:642px"></span>
</section>

<footer class="footer">
  <svg class="abs" style="left:0;top:3380px" width="1200" height="534" viewBox="0 0 1200 534">
    <path d="M0,30 C300,120 700,150 1200,40 L1200,534 L0,534 Z" fill="var(--orange)"/>
    <path d="M0,20 C300,110 700,140 1200,30 L1200,50 C700,165 300,135 0,44 Z" fill="var(--sky)"/>
    <path d="M0,44 C300,135 700,165 1200,50 L1200,60 C700,175 300,145 0,56 Z" fill="var(--navy)"/>
  </svg>
  <div class="ph" role="img" aria-label="Character mascot holding shaved ice" style="left:1020px;top:3278px;width:170px;height:205px;background:linear-gradient(135deg,#2e9be0,#f27d3a)"></div>

  <div class="footer-brand"><div class="name">GLIMMERCUP</div><div class="tag">The Coolest Treats</div></div>
  <span class="footer-rule" style="left:392px"></span>
  <span class="footer-rule" style="left:650px"></span>
  <span class="footer-rule" style="left:939px"></span>

  <h4 class="footer-head" style="left:426px">Quick Links</h4>
  <span class="footer-link" style="left:426px;top:3640px">Home</span>
  <span class="footer-link" style="left:426px;top:3676px">About Us</span>
  <span class="footer-link" style="left:426px;top:3712px">Menu</span>
  <span class="footer-link" style="left:426px;top:3748px">Events</span>

  <h4 class="footer-head" style="left:685px">Contact Us</h4>
  <span class="footer-icon" style="left:686px;top:3640px"><svg width="16" height="16" viewBox="0 0 24 24"><path d="M6.6 10.8a15 15 0 006.6 6.6l2.2-2.2a1 1 0 011-.25 11.4 11.4 0 003.6.57 1 1 0 011 1V20a1 1 0 01-1 1A17 17 0 013 4a1 1 0 011-1h3.5a1 1 0 011 1 11.4 11.4 0 00.57 3.6 1 1 0 01-.25 1z" fill="#1c1c1c"/></svg></span>
  <span class="footer-link" style="left:730px;top:3647px">555-014-2290</span>
  <span class="footer-icon" style="left:686px;top:3694px"><svg width="14" height="18" viewBox="0 0 24 30"><path d="M12 0a10 10 0 00-10 10c0 7.5 10 20 10 20s10-12.5 10-20A10 10 0 0012 0zm0 14a4 4 0 110-8 4 4 0 010 8z" fill="#1c1c1c"/></svg></span>
  <span class="footer-link" style="left:730px;top:3690px;width:170px;line-height:22px">48 Snowcone Way, Chillbrook, CA 90000</span>

  <h4 class="footer-head" style="left:975px">Follow Us On</h4>
  <span class="footer-icon" style="left:976px;top:3640px"></span>
  <span class="footer-link" style="left:1020px;top:3647px">Friendpage</span>
  <span class="footer-icon" style="left:976px;top:3690px"></span>
  <span class="footer-link" style="left:1020px;top:3697px">Snapgallery</span>

  <span class="abs" style="left:112px;top:3836px;width:975px;height:1px;background:rgba(0,0,0,.25)"></span>
  <p class="copyright">Copyright © 2025 Glimmercup - All Rights Reserved.</p>
</footer>

</body>
</html>
```